Home inspection business! professional look attracting customers just by looks. Read must haves

its a new business I started on my own for home inspections I would like something very professional to give to real estate agents and clients, its going to have my license number on it my business phone number my name my website as well etc on the back side it will be servicing areas and also what kind of services I offer I also have a business card from someone else the way I would like mine to be. I will attach my logo

Home Inspection

listed in nice to haves

• phone number - 555 293 8471
• website- hollowpinecheck.com
• license number #2938475610
• my name Gavin keropulis
• picture of my logo and me on the front
• on the back of the card. stating I am servicing All of New York and Long Island
• also services I will offer will be home inspection -mold inspection -lead inspection -radon inspection -Termite Inspection -Infared Scan.
• and also we provide inspections for single family homes condos co-ops town-homes
• and commercial property
• same colors as the logos and also if you recommend fonts to look like the logo not sure up to you

```html
<!DOCTYPE html>
<html lang="en">
<head>
<meta charset="utf-8">
<title>Hollow Pine Home Inspectors – Business Card</title>
<link rel="stylesheet" href="https://fonts.googleapis.com/css2?family=Montserrat:wght@500;600;700&family=Roboto:wght@400;500&display=swap">
<style>
  :root {
    --backdrop: #d1d2d4;
    --card-white: #ffffff;
    --brand-blue: #52a3db;
    --brand-gray: #6d6e71;
    --band-gray: #747578;
    --text-dark: #4a4b4e;
    --white: #ffffff;
  }
  * { margin: 0; padding: 0; box-sizing: border-box; }
  html, body {
    width: 1200px; height: 1200px; overflow: hidden;
    background: var(--backdrop);
  }
  .stage { position: relative; width: 1200px; height: 1200px; }
  .card {
    position: absolute; left: 194px; width: 812px; height: 464px;
    border-radius: 8px; overflow: hidden;
    box-shadow: 6px 7px 10px rgba(0,0,0,0.28);
  }
  .card-front { top: 125px; background: var(--card-white); }
  .card-back { top: 611px; background: var(--brand-blue); }

  .portrait {
    position: absolute; left: 0; top: 50px; width: 330px; height: 414px;
    background: linear-gradient(180deg, #e6dfdc 0%, #b9a9a3 30%, #3b3f4a 55%, #262a33 100%);
  }
  .license-band {
    position: absolute; left: 330px; right: 0; bottom: 0; height: 55px;
    background: var(--band-gray);
    color: var(--white);
    font: 500 21px/55px "Montserrat", sans-serif;
    padding-left: 74px;
  }

  .brand-front {
    position: absolute; left: 390px; top: 72px; width: 400px;
    display: flex; align-items: center; gap: 14px;
    color: var(--brand-gray);
    font-family: "Montserrat", sans-serif; font-weight: 700;
  }
  .brand-dot { width: 46px; height: 46px; border-radius: 50%; background: var(--brand-blue); flex: none; }
  .brand-name { font-size: 31px; line-height: 1.15; letter-spacing: 0.5px; }
  .brand-name span { display: block; font-size: 17px; letter-spacing: 5px; }

  .contact-block { position: absolute; left: 410px; top: 235px; font-family: "Montserrat", sans-serif; }
  .person-name { color: var(--brand-blue); font-size: 26px; font-weight: 600; letter-spacing: 0.5px; }
  .person-title { color: var(--text-dark); font-size: 19px; font-weight: 600; margin-top: 2px; }
  .contact-list { list-style: none; margin-top: 18px; }
  .contact-list li {
    display: flex; align-items: center; gap: 8px;
    color: var(--text-dark); font-size: 21px; font-weight: 500; height: 30px;
  }
  .contact-list svg { width: 20px; height: 20px; flex: none; }

  .brand-back {
    position: absolute; left: 0; right: 0; top: 80px;
    display: flex; justify-content: center; align-items: center; gap: 18px;
    color: var(--white);
    font-family: "Roboto", sans-serif; font-weight: 500;
  }
  .brand-back .brand-dot { width: 60px; height: 60px; background: var(--white); }
  .brand-back .brand-name { font-size: 46px; }
  .brand-back .brand-name span { font-size: 24px; letter-spacing: 8px; }

  .service-area {
    position: absolute; left: 0; right: 0; top: 264px; text-align: center;
    color: var(--white); font: 500 24px/1 "Roboto", sans-serif;
  }
  .service-list {
    position: absolute; left: 0; right: 0; top: 304px; text-align: center;
    color: var(--white); font: 400 20px/29.5px "Roboto", sans-serif;
  }
</style>
</head>
<body>
<div class="stage">
  <section class="card card-front">
    <div class="portrait" role="img" aria-label="Portrait photo of the inspector in a dark suit and tie, arms crossed"></div>

    <div class="brand-front">
      <div class="brand-dot"></div>
      <div class="brand-name">HOLLOW PINE<span>HOME INSPECTORS</span></div>
    </div>

    <div class="contact-block">
      <div class="person-name">GAVIN KEROPULIS</div>
      <div class="person-title">Director</div>
      <ul class="contact-list">
        <li>
          <svg viewBox="0 0 20 20"><path fill="#52a3db" d="M2 7c0-2 3-4 8-4s8 2 8 4v1.5h-4V7c-1-.8-6-.8-8 0v1.5H2zM5 10h10l2 7H3z"/><circle cx="10" cy="13.5" r="2" fill="#fff"/></svg>
          555 293 8471
        </li>
        <li>
          <svg viewBox="0 0 20 20"><rect x="1" y="4" width="18" height="12" rx="1" fill="#52a3db"/><path d="M2 5l8 6 8-6" fill="none" stroke="#fff" stroke-width="1.4"/></svg>
          info@hollowpinecheck.com
        </li>
        <li>
          <svg viewBox="0 0 20 20"><circle cx="10" cy="10" r="9" fill="#52a3db"/><path d="M6 5c2 1 1 3 3 3s1 3 0 4-1 3-2 4M13 4c-1 2 1 3 2 4s1 3-1 4" fill="none" stroke="#fff" stroke-width="1.3"/></svg>
          www.hollowpinecheck.com
        </li>
      </ul>
    </div>

    <div class="license-band">License Number #2938475610</div>
  </section>

  <section class="card card-back">
    <div class="brand-back">
      <div class="brand-dot"></div>
      <div class="brand-name">HOLLOW PINE<span>HOME INSPECTORS</span></div>
    </div>

    <p class="service-area">We are servicing All of New York and Long Island</p>
    <p class="service-list">
      ● Home Inspection ● Mold Inspection<br>
      ● Lead Inspection ● Radon Inspection ● Termite Inspection ● Infared Scan.<br>
      We provide inspections for single family homes&nbsp; condos co-ops<br>
      town-homes and commercial property
    </p>
  </section>
</div>
</body>
</html>
```